Office Building Banner

Need a 4x8 vinyl banner made for our office/storage headquarters. Our branded colors and logo can be taken from our website, www.halvenroofingtx.com. All other elements of our brand have not been decided on yet, so you have creative autonomy there. Our location faces a busy highway in Seguin, Texas, so the banner needs to have our contact information and full name clearly seen from a bit away's away, hope that makes sense. Our company wants to convey attributes of strength, loyalty, protection - basically emulating the qualities of a wolf and his pack. I have uploaded a few items we have been using to date, but as you can see, graphic design is not our forte.

```html
<!DOCTYPE html>
<html lang="en">
<head>
<meta charset="utf-8">
<title>Halven Roofing &amp; Renovations – Office Banner</title>
<link rel="stylesheet" href="https://fonts.googleapis.com/css2?family=Poppins:wght@500;600;700;800&display=swap">
<style>
  :root {
    --orange: #f37f21;
    --ink: #1e1e1e;
    --band: #e2e3e5;
    --paper: #ffffff;
    --rule: #c9c9c9;
    --emblem: #ececec;
  }
  html, body {
    margin: 0;
    padding: 0;
    width: 1200px;
    height: 601px;
    overflow: hidden;
    background: var(--paper);
  }
  .banner {
    position: relative;
    width: 1200px;
    height: 601px;
    overflow: hidden;
    background: var(--paper);
    font-family: "Poppins", sans-serif;
    color: var(--ink);
  }
  .side-shape {
    position: absolute;
    inset: 0;
    width: 1200px;
    height: 601px;
  }
  .brand {
    position: absolute;
    left: 18px;
    top: 60px;
    width: 392px;
    text-align: center;
  }
  .brand-circle {
    display: block;
    margin: 0 auto 28px;
    width: 200px;
    height: 200px;
    border-radius: 50%;
    background: var(--emblem);
  }
  .brand-name {
    margin: 0;
    font-weight: 800;
    color: var(--ink);
    line-height: 1;
  }
  .brand-name .main {
    display: block;
    font-size: 74px;
    letter-spacing: 1px;
  }
  .brand-name .sub {
    display: block;
    margin-top: 10px;
    font-size: 19.5px;
    letter-spacing: 0.5px;
  }
  .content {
    position: absolute;
    left: 506px;
    top: 0;
    width: 641px;
    height: 601px;
  }
  .headline {
    position: absolute;
    left: 0;
    top: 72px;
    width: 641px;
    margin: 0;
    text-align: justify;
    text-align-last: justify;
    font-weight: 700;
    font-size: 40px;
    line-height: 1;
    white-space: nowrap;
  }
  .subline {
    position: absolute;
    left: 0;
    top: 118px;
    width: 641px;
    margin: 0;
    text-align: justify;
    text-align-last: justify;
    font-weight: 600;
    font-size: 25px;
    line-height: 1;
    white-space: nowrap;
  }
  .services {
    position: absolute;
    top: 206px;
    left: 0;
    width: 641px;
    margin: 0;
    padding: 0;
    list-style: none;
  }
  .service {
    position: absolute;
    top: 0;
    width: 200px;
    margin-left: -100px;
    text-align: center;
  }
  .service svg {
    display: block;
    margin: 0 auto;
    width: 60px;
    height: 60px;
  }
  .service-label {
    display: block;
    margin-top: 8px;
    font-weight: 600;
    font-size: 20px;
    letter-spacing: 0.3px;
    white-space: nowrap;
  }
  .service--roofing { left: 109px; }
  .service--turn { left: 304px; }
  .service--renovation { left: 511px; }
  .divider {
    position: absolute;
    left: 0;
    top: 362px;
    width: 641px;
    height: 1px;
    margin: 0;
    border: 0;
    background: var(--rule);
  }
  .website {
    position: absolute;
    left: 0;
    top: 414px;
    width: 641px;
    margin: 0;
    text-align: center;
    font-weight: 600;
    font-size: 32px;
    line-height: 1;
  }
  .call {
    position: absolute;
    left: 0;
    top: 486px;
    width: 641px;
    margin: 0;
    text-align: right;
    font-weight: 600;
    font-size: 42px;
    line-height: 1;
    white-space: nowrap;
  }
  .call .phone {
    color: var(--orange);
    font-weight: 700;
  }
  .icon-stroke {
    fill: none;
    stroke: var(--orange);
    stroke-width: 2.6;
    stroke-linecap: round;
    stroke-linejoin: round;
  }
</style>
</head>
<body>
<main class="banner">
  <svg class="side-shape" viewBox="0 0 1200 601" aria-hidden="true">
    <path d="M0 0 H378 C444 60 494 160 480 240 C469 330 424 380 432 460 C436 520 464 570 486 601 H0 Z" fill="var(--band)"/>
    <path d="M0 0 H354 C420 60 470 160 456 240 C445 330 400 380 408 460 C412 520 440 570 462 601 H0 Z" fill="var(--orange)"/>
  </svg>

  <div class="brand">
    <span class="brand-circle" aria-hidden="true"></span>
    <p class="brand-name">
      <span class="main">HALVEN</span>
      <span class="sub">ROOFING &amp; RENOVATIONS</span>
    </p>
  </div>

  <section class="content">
    <h1 class="headline">A TOTAL SOLUTIONS PARTNER</h1>
    <p class="subline">FOR ALL YOUR HOME IMPROVEMENTS NEEDS</p>

    <ul class="services">
      <li class="service service--roofing">
        <svg viewBox="0 0 60 60" aria-hidden="true">
          <path class="icon-stroke" d="M3 40 L30 14 L57 40"/>
          <path class="icon-stroke" d="M4 34 L22 12 L44 12"/>
          <path class="icon-stroke" d="M10 27 H34 M15 21 H38 M20 15 H42"/>
          <path class="icon-stroke" d="M18 14 L10 34 M27 13 L18 34 M36 13 L26 30"/>
          <path class="icon-stroke" d="M8 40 V48 M43 36 V48 M52 40 V48"/>
        </svg>
        <span class="service-label">ROOFING</span>
      </li>
      <li class="service service--turn">
        <svg viewBox="0 0 60 60" aria-hidden="true">
          <path class="icon-stroke" d="M10 6 A8 8 0 0 0 8 18 L40 50 A4 4 0 0 0 47 44 L16 12 A8 8 0 0 0 10 6 Z"/>
          <path class="icon-stroke" d="M50 6 L55 11 L49 17 L44 16 L22 38 L24 42 L16 52 L8 44 L18 36 L22 37 L44 15 L43 12 Z"/>
        </svg>
        <span class="service-label">TURN SERVICES</span>
      </li>
      <li class="service service--renovation">
        <svg viewBox="0 0 60 60" aria-hidden="true">
          <path class="icon-stroke" d="M14 10 A27 27 0 1 1 8 20"/>
          <path class="icon-stroke" d="M8 6 L14 10 L10 16"/>
          <path class="icon-stroke" d="M18 30 L30 19 L42 30 M21 28 V42 H39 V28"/>
          <path class="icon-stroke" d="M27 42 V34 H33 V42"/>
        </svg>
        <span class="service-label">REVOVATION</span>
      </li>
    </ul>

    <hr class="divider">

    <p class="website">www.halvenroofingtx.com</p>
    <p class="call">CALL US TODAY <span class="phone">512-555-0148</span></p>
  </section>
</main>
</body>
</html>
```